■依頼の目的/概要
鶏白湯塩ラーメンのポスター作成お願いします!

■依頼詳細
鶏白湯塩ラーメンのポスターを作成お願いします。
値段は780円です。

デザインについては特に、指定はありません。
A1のポスターです。

鶏白湯塩ラーメンについて

鶏白湯スープにじっくり時間をかけて熟成させた自家製塩タレを合わせ、アクセントにアオサを使用しました。
(こちらの文章を入れて欲しいです。)

写真はURLからダウンロードお願いします。

http://filebako.example/dl/7a1c93e0b5d2f4c8a6e1027b3d9f5c4e8a1b6d20

お店のイメージです。
こちらのお店の物になります。

https://gurumemo.example/fukuoka/B7002/B700209/51178364/

https://www.tomobook.example/torisoba.hakata/
http://filebako.example/dl/3e8d21f6c0a94b7e5d13a8f2c6b0e974d1a5c3b8

おそくなりましたこちらからダウンロードお願いしいます。
再度アップしました。こちらからダウンロードできますか?
http://filebako.example/dl/c5b07e3a91d6f2e48a0c7b15d3e9f6a2b4c81d07

とても素晴らしいデザインありがとうございます!

提案ありがとうございました!

```html
<!DOCTYPE html>
<html lang="ja">
<head>
<meta charset="utf-8">
<title>鶏白湯塩ラーメン 780円</title>
<link rel="stylesheet" href="https://fonts.googleapis.com/css2?family=Dela+Gothic+One&family=Noto+Sans+JP:wght@700;900&display=swap">
<style>
  :root {
    --ink: #141414;
    --accent-red: #d3141c;
    --salt-blue: #1f5fa8;
    --badge-orange: #e8641a;
    --paper: #ffffff;
    --wood-light: #d9b48a;
    --wood-mid: #a8703f;
    --wood-dark: #6b3f1f;
    --soup: #f4efe6;
  }
  * { margin: 0; padding: 0; box-sizing: border-box; }
  html, body { width: 847px; height: 1200px; overflow: hidden; background: #ffffff; }
  .poster {
    position: relative;
    width: 847px;
    height: 1200px;
    overflow: hidden;
    font-family: "Noto Sans JP", sans-serif;
    color: var(--ink);
  }
  .photo {
    position: absolute;
    inset: 0;
    background:
      radial-gradient(ellipse 390px 280px at 395px 830px, #ffffff 0%, var(--soup) 60%, #e6ddcf 76%, rgba(230,221,207,0) 79%),
      linear-gradient(180deg, #ffffff 0%, #fbf6f0 24%, #efdcc4 36%, var(--wood-light) 50%, var(--wood-mid) 76%, var(--wood-dark) 100%);
  }
  .title {
    position: absolute;
    left: 112px;
    top: 40px;
    font-family: "Noto Sans JP", sans-serif;
    font-weight: 900;
    line-height: 1;
  }
  .title-main {
    display: block;
    font-size: 124px;
    letter-spacing: 2px;
    color: var(--ink);
  }
  .title-sub {
    display: block;
    margin-top: 18px;
    font-size: 120px;
    letter-spacing: -2px;
    color: var(--salt-blue);
  }
  .description {
    position: absolute;
    left: 262px;
    width: 550px;
    top: 366px;
    text-align: center;
    font-size: 15px;
    font-weight: 700;
    line-height: 1.6;
    color: var(--ink);
  }
  .badge {
    position: absolute;
    left: 72px;
    top: 422px;
    width: 128px;
    height: 128px;
    border-radius: 50%;
    background: var(--badge-orange);
    color: var(--paper);
    display: flex;
    flex-direction: column;
    align-items: center;
    justify-content: center;
    font-weight: 900;
    text-align: center;
    line-height: 1.15;
  }
  .badge-small { font-size: 14px; }
  .badge-large { font-size: 27px; margin-top: 4px; }
  .badge-large + .badge-large { margin-top: 0; font-size: 25px; }
  .brand {
    position: absolute;
    left: 84px;
    top: 1054px;
    display: flex;
    align-items: center;
    gap: 10px;
    color: var(--paper);
    font-weight: 900;
    font-size: 30px;
    line-height: 1.1;
  }
  .brand-dot {
    width: 24px;
    height: 24px;
    border-radius: 50%;
    background: var(--paper);
  }
  .price {
    position: absolute;
    right: 22px;
    top: 1020px;
    font-family: "Dela Gothic One", sans-serif;
    font-size: 90px;
    color: var(--accent-red);
    line-height: 1;
    text-shadow: 3px 3px 0 var(--paper), -3px -3px 0 var(--paper), 3px -3px 0 var(--paper), -3px 3px 0 var(--paper);
  }
  .price .yen { font-size: 64px; }
</style>
</head>
<body>
  <main class="poster">
    <div class="photo" role="img" aria-label="木目のテーブルに置かれた鶏白湯塩ラーメンの写真。白いスープにアオサ、白髪ねぎ、チャーシュー、箸で持ち上げた麺"></div>

    <h1 class="title">
      <span class="title-main">鶏白湯</span>
      <span class="title-sub">塩ラーメン</span>
    </h1>

    <p class="description">鶏白湯スープにじっくり時間をかけて熟成させた自家製塩タレを合わせ、<br>アクセントにアオサを使用しました。</p>

    <div class="badge">
      <span class="badge-small">アクセントに</span>
      <span class="badge-large">アオサ</span>
      <span class="badge-large">使用</span>
    </div>

    <div class="brand">
      <span class="brand-dot" aria-hidden="true"></span>
      <span>鶏そば<br>TORIHAKU</span>
    </div>

    <p class="price">780<span class="yen">円</span></p>
  </main>
</body>
</html>
```